Automotive Repair Christmas Incentive Offer

We are an automotive repair shop that specializes in import auto repair. We need a postcard mailer that will target pre-existing customers for the Holiday season. On the front, we would like an image of a happy, female customer that is pointing to a message of holiday wishes with our company. The colors should be a traditional holiday theme with the predominant color being red. We would like the visual trail to start at the female's face and then travel to her finger pointing to the Happy Holidays message. On the reverse side, we would like to have the text read like the attached PDF file.

Target Market(s)

Females, 25-45, average household income $100000.00/year, college educated, kids in famile

Industry/Entity Type

Automotive

Font styles to use
Serif

Colors
ec1f27
9bcb3c
000000

Requirements
Must have
• Simple lines, clear and attractive font, be NPDS approved format for mailing, attractive images that are polished looking and high-quality, holiday colors
Should not have
• Cluttered images, hard to read font, complicated color schemes

```html
<!DOCTYPE html>
<html lang="en">
<head>
<meta charset="utf-8">
<title>Harlow Auto – Holiday Gift Postcard</title>
<link rel="stylesheet" href="https://fonts.googleapis.com/css2?family=Roboto+Condensed:wght@400;700&family=Questrial&family=Arimo:wght@400;700&display=swap">
<style>
  :root {
    --red: #a81e27;
    --red-dark: #6e1016;
    --white: #ffffff;
    --ink: #222222;
    --stage: #2b2b2b;
    --rule: #8a8a8a;
  }
  * { margin: 0; padding: 0; box-sizing: border-box; }
  html, body { width: 900px; height: 1200px; overflow: hidden; }
  body { background: var(--stage); position: relative; font-family: "Questrial", Arial, sans-serif; }

  .postcard { position: absolute; left: 95px; width: 710px; height: 458px; overflow: hidden; background: var(--white); }
  .postcard--front { top: 130px; }
  .postcard--back { top: 622px; }

  /* Front */
  .hero-photo { position: absolute; inset: 0;
    background: radial-gradient(ellipse at 38% 45%, #f3dcc4 0%, #eadbc6 18%, rgba(240,236,228,0) 40%),
                linear-gradient(120deg, #f4f4f2 0%, #e9ebe6 40%, #c9d6b0 62%, #eef0ec 80%, #e2e2e2 100%); }
  .front-shapes { position: absolute; inset: 0; }
  .front-title { position: absolute; left: 298px; top: 18px; font-family: "Roboto Condensed", Arial, sans-serif; font-weight: 700; font-size: 37px; color: var(--red); letter-spacing: 2.4px; white-space: nowrap; }
  .offer { position: absolute; right: 16px; top: 138px; text-align: right; color: var(--white); }
  .offer-amount { font-size: 74px; line-height: 74px; }
  .offer-line1 { font-size: 34px; line-height: 36px; font-weight: 700; -webkit-text-stroke: 0.6px var(--white); }
  .offer-line2 { font-size: 30px; line-height: 38px; }
  .brand { position: absolute; left: 28px; top: 372px; display: flex; align-items: center; gap: 10px; }
  .brand-mark { width: 18px; height: 18px; background: var(--red); }
  .brand-name { font-family: "Roboto Condensed", Arial, sans-serif; font-weight: 700; font-size: 34px; color: var(--ink); letter-spacing: 1px; }

  /* Back */
  .back-shapes { position: absolute; inset: 0; }
  .back-content { position: absolute; left: 0; top: 0; width: 420px; height: 100%; color: var(--white); }
  .back-title { position: absolute; left: 48px; top: 20px; width: 270px; font-family: "Arimo", Arial, sans-serif; font-weight: 700; font-size: 24px; text-align: center; white-space: nowrap; padding-bottom: 2px; border-bottom: 1.5px solid var(--white); }
  .message { position: absolute; left: 18px; top: 65px; font-size: 15px; line-height: 18.5px; white-space: nowrap; }
  .contact-label { position: absolute; left: 18px; top: 188px; width: 142px; height: 27px; background: var(--white); color: var(--red); font-family: "Arimo", Arial, sans-serif; font-weight: 700; font-size: 18px; padding: 3px 6px; }
  .contact-address { position: absolute; left: 20px; top: 223px; font-size: 16px; line-height: 20px; }
  .contact-lines { position: absolute; left: 20px; top: 308px; font-size: 16px; line-height: 21px; }
  .contact-lines div { display: flex; align-items: center; gap: 3px; }
  .contact-lines svg { width: 13px; height: 13px; }
  .call { position: absolute; left: 100px; top: 362px; font-family: "Arimo", Arial, sans-serif; font-size: 30px; line-height: 32px; white-space: nowrap; }
  .call-sub { position: absolute; left: 135px; top: 395px; font-family: "Arimo", Arial, sans-serif; font-size: 18px; white-space: nowrap; }
  .fine-print { position: absolute; left: 9px; top: 428px; font-size: 6.6px; line-height: 9px; white-space: nowrap; }
  .stamp-box { position: absolute; left: 599px; top: 23px; width: 91px; height: 71px; border: 1px solid var(--ink); }
  .address-line { position: absolute; left: 421px; width: 271px; height: 0; border-top: 1px solid var(--rule); }
</style>
</head>
<body>

<section class="postcard postcard--front">
  <div class="hero-photo" role="img" aria-label="Photo of a smiling woman in a wide sun hat and sunglasses waving from a white convertible"></div>
  <svg class="front-shapes" viewBox="0 0 710 458" aria-hidden="true">
    <polygon points="676,17 417,250 690,450" fill="var(--red-dark)"/>
    <polygon points="710,32 440,250 710,458" fill="var(--red)"/>
  </svg>
  <h1 class="front-title">OUR HOLIDAY GIFT</h1>
  <div class="offer">
    <div class="offer-amount">$25</div>
    <div class="offer-line1">off your</div>
    <div class="offer-line2">next service.</div>
  </div>
  <div class="brand">
    <span class="brand-mark"></span>
    <span class="brand-name">HARLOW</span>
  </div>
</section>

<section class="postcard postcard--back">
  <svg class="back-shapes" viewBox="0 0 710 458" aria-hidden="true">
    <polygon points="0,0 427,0 325,458 0,458" fill="var(--red)"/>
  </svg>
  <div class="back-content">
    <h2 class="back-title">OUR HOLIDAY GIFT</h2>
    <p class="message">We, at Harlow Auto, would like to give thanks<br>for all of your patronage and support<br>over the past year.<br>In appreciation for letting us take care of your<br>vehicle, we’d like to give you a gift of<br>$25.00 off your next service.</p>
    <div class="contact-label">Contact Us:</div>
    <p class="contact-address">The Harlow Family,<br>Harlow Auto<br>4120 Birch Hwy<br>Larkton, AK 99601</p>
    <div class="contact-lines">
      <div><svg viewBox="0 0 24 24" aria-hidden="true"><path fill="#fff" d="M6.6 10.8a15.1 15.1 0 0 0 6.6 6.6l2.2-2.2a1 1 0 0 1 1-.25 11.4 11.4 0 0 0 3.6.57 1 1 0 0 1 1 1V20a1 1 0 0 1-1 1A17 17 0 0 1 3 4a1 1 0 0 1 1-1h3.5a1 1 0 0 1 1 1c0 1.25.2 2.45.57 3.57a1 1 0 0 1-.25 1z"/></svg>907-555-0142</div>
      <div><svg viewBox="0 0 24 24" aria-hidden="true" fill="none" stroke="#fff" stroke-width="2"><circle cx="12" cy="12" r="10"/><ellipse cx="12" cy="12" rx="4.5" ry="10"/><line x1="2" y1="12" x2="22" y2="12"/></svg>harlowimportauto.com</div>
    </div>
    <div class="call">Call: 555-0142</div>
    <div class="call-sub">for your appointment</div>
    <p class="fine-print">* This coupon may be transferred to a friend or family member. Limit one coupon<br>per customer. Coupon does not have a cash value. Not valid with any other special.</p>
  </div>
  <div class="stamp-box"></div>
  <div class="address-line" style="top:258px"></div>
  <div class="address-line" style="top:304px"></div>
  <div class="address-line" style="top:350px"></div>
</section>

</body>
</html>
```